***Retail Packaging Card Design VERY SIMPLE FAST MONEY

Hey guys and gals...

I own a company that makes embroidered patches. We are getting ready to package our item for display in stores. To do so, we have these cool poly bags that seal at the bottom and then have a built-in hole at the top. All you need to do is insert the pre-printed cardstock card and the patch, and it is ready to hang on a wire retail rack.

We have two size bags, and the cards that fit in each will be:
4.25 inches wide x 5.5 inches tall
and
3.25 inches wide x 5.25 inches tall.

Once you have the patch inside, with the card, you are really only working with an available 1.5-inch section above that patch that shows. See examples below.

What I need: some designs for this card that will work with the various types of patches we make. I am willing to pick more than one winner and more than one design if more than one of these works out. I have five themes in mind, and if they are good enough, I am willing to buy all five separately.

First of all, the wording in the design is simply: IRON-ON PATCH.

From there, we want versions of this design that would look right on the following types of patches:

1) American Flag/Patriotic - this would be for a flag you might buy in a military surplus store or in a souvenir store in a city.

2) Rock and Roll - something that might work in a Marlowe's Novelties type of setting - imagine a biohazard patch or a skull and crossbones in the packaging.

3) Scuba Diving. We actually sell a ton of Scuba-related/Diver Down patches and need something specific to those types of stores.

4) Irish patches. Something with a Celtic and/or Ireland design would be great.

5) Generic International Flags. Instead of just one country flag, something that could easily be pictured housing the flag of any country. Some of our stores carry 50-60 styles here, so something that might work with all of them.

One of my main objectives with this product is that the logo/design be EASY TO READ. Imagine walking through a Marlowe's Novelties, a head shop, or an airport gift shop. These will be hanging on a wire rack, and that IRON-ON PATCH must be really easy to read. (That's why we're not doing Embroidered Patch for the text - the word Embroidered is just too hard to read from 5-8 feet and/or looks to squished in). Therefore, I would think the wording would take up a majority of the limited space.

The only other design tip I have is to avoid a white background. One of the sample I will upload has a white background, but a pattern or even just the plain black looks better with a patch inside.

Below I am attaching a few photo links - a couple of really generic mock-ups we did ourselves (they are serviceable but lack any real character, style, or look like they "fit" one of the categories above). I'm also attaching a photo of something similar that a competitor does, just so you can see a patch inside packaging an get a sense of what the final product might look like.

Some very generic mock-ups we've been working with:
http://brindlewoodgoods.example/misc/hangers3.jpg

What these look like with the patches in them:
http://brindlewoodgoods.example/misc/sample1.jpg
http://brindlewoodgoods.example/misc/sample2.jpg

A sample of a competitor's product inside bag with card similar to what you might design:

http://brindlewoodgoods.example/misc/USFLAG.jpg

If you have any questions, or if I have left anything out, please ask and I will post your answer here.

December 18 UPDATE TO DESIGNERS: We have some really good entries in for the "rock" and "patriotic" categories. If you want to submit on these, we encourage more designs, but bring your best. As for Irish, Scuba, and some sort of "works with any flag" category are still somewhat open (especially the first two). Would like to see something on the irish that incorporates either a clover (we sell one at keepsakestitch dot example that would be a good shape/style to use) or the Irish flag or Irish harp. As for the scuba, something red-themed possibly with the red Diver Down flag would be nice.

Requirements
Must have
• Easy to read
Should not have
• Anything too busy to affect readability. Especially any font that is too fancy. Size it to actual size on your screen, stand up and step back 5-8 feet. Is it a blur? Change it.

```html
<!DOCTYPE html>
<html lang="en">
<head>
<meta charset="utf-8">
<title>Iron-On Patch Packaging Card – Patriotic</title>
<link rel="stylesheet" href="https://fonts.googleapis.com/css2?family=Fredoka:wght@700&display=swap">
<style>
  :root {
    --flag-blue: #7a7eb3;
    --flag-red: #ee8c91;
    --flag-white: #ffffff;
    --title-red: #e11d2b;
    --title-navy: #262c82;
    --title-outline: #ffffff;
    --title-shadow: rgba(40, 20, 40, 0.35);
  }
  html, body {
    margin: 0;
    padding: 0;
    width: 744px;
    height: 1200px;
    overflow: hidden;
    background: #ffffff;
  }
  .card {
    position: relative;
    width: 744px;
    height: 1200px;
    overflow: hidden;
  }
  .flag-backdrop {
    position: absolute;
    inset: 0;
    background:
      radial-gradient(ellipse 560px 480px at 180px 300px, var(--flag-blue) 0%, rgba(122,126,179,0.85) 55%, rgba(122,126,179,0) 100%),
      linear-gradient(160deg, var(--flag-red) 0%, #f6c3c6 35%, var(--flag-white) 55%, #f4b3b7 75%, var(--flag-red) 100%);
  }
  .title {
    position: absolute;
    left: 0;
    right: 0;
    top: 12px;
    margin: 0;
    font-family: "Fredoka", "Arial Rounded MT Bold", sans-serif;
    font-weight: 700;
    text-align: center;
    line-height: 0.92;
    letter-spacing: -2px;
    text-transform: uppercase;
  }
  .title-line {
    display: block;
    -webkit-text-stroke: 22px var(--title-outline);
    paint-order: stroke fill;
    filter: drop-shadow(6px 8px 6px var(--title-shadow));
  }
  .title-line--top {
    color: var(--title-red);
    font-size: 158px;
  }
  .title-line--bottom {
    color: var(--title-navy);
    font-size: 150px;
  }
</style>
</head>
<body>
  <main class="card">
    <div class="flag-backdrop" role="img" aria-label="Waving American flag with blue star field and red and white stripes"></div>
    <h1 class="title">
      <span class="title-line title-line--top">Iron-On</span>
      <span class="title-line title-line--bottom">Patch</span>
    </h1>
  </main>
</body>
</html>
```